a board game needs a good card design (5 cards in the same design)

We need a redesign for our cards.
Each card file is 63*88mm, 3mm bleeds - 69mm*94mm, should be done vector and CMYK, because it will be printed.

The game includes 108 cards (don't worry, no needs to design them all), it has:
numbers from 1 to 20 on the yellow background
from 6 to 20 on the green background
+1, +2, +3, +4, +5 on the white background with our logo,
special card on blue background (now it's "+", but it's not necessary, it could be anything with positive meaning, because it's kind of joker card)
circle on red background. We don't want see this circle anymore, it should be replaced to something else. It's the worst card, so the player who draws should understand "oops, that's not good!".

What we need:
now cards look boring and simple, it should look funnier, people hold them and know it's a fun game.
We expect in return 5 cards:
1) any number on the green background
2) any number on the yellow bg.
3) +5 on the white bg with our logo. The white card means the next person should PILE UP, so we're fine with our logo on the background, but if you can make up something more interesting, would be great.
4) something on the red bg, what means danger, for a card which could be hard to get rid of
5) something positive on the blue bg, what means you have 2 turns instead of 1, can play this card on any card and place any card on top of it (could sound complicated, just know it's a good card to have)

I've written "color of the background", but these colors are not necessary to come from the background, just overall color of the card should have these primary colors.

All cards should have a big number or whatever in the center and small copies in 2 corners as on standard cards.

Would be great to not make your own font for digits, because we should be able to copy the design to all numbers used.

I have uploaded our logo and current basic design of our cards.

Target Market(s)

the game is suitable for meetup with friends or family play. So it could be anyone from 7 years old to 99

Font styles to use
Sans Serif

Colors
0792cd
ec1f27
fbed22
ffffff
9bcb3b

Requirements
Must have
• the cards must have a number or symbol in the center and on 2 corners (upside down on the bottom corner). Each card must have primary color.
Nice to have
• something on the background, not just color-background. Please use the logo for the background for the white card only.
Should not have
• words, animals, flowers etc
• symbols and digits only please.

```html
<!DOCTYPE html>
<html lang="en">
<head>
<meta charset="utf-8">
<title>Card Set: Green 7, Yellow 12, White +5, Red Danger, Blue Joker</title>
<link href="https://fonts.googleapis.com/css2?family=Titan+One&display=swap" rel="stylesheet">
<style>
  :root {
    --stage: #3a3a3c;
    --card-border: #ffffff;
    --green: #7fbf4d;
    --yellow: #fbe82c;
    --white-panel: #f2f2f2;
    --red: #ec2f2a;
    --blue: #4a80c4;
    --ink-blue: #3d78c2;
    --outline: #000000;
    --rim: #ffffff;
  }
  * { margin: 0; padding: 0; box-sizing: border-box; }
  html, body {
    width: 1200px;
    height: 376px;
    overflow: hidden;
    background: var(--stage);
  }
  .card-row {
    position: relative;
    width: 1200px;
    height: 376px;
  }
  .card {
    position: absolute;
    top: 56px;
    width: 193px;
    height: 269px;
    border-radius: 10px;
    background: var(--card-border);
    box-shadow: 0 4px 10px rgba(0,0,0,0.45);
  }
  .card svg { display: block; width: 193px; height: 269px; }
  .card--green  { left: 61px; }
  .card--yellow { left: 285px; }
  .card--white  { left: 509px; }
  .card--red    { left: 733px; }
  .card--blue   { left: 957px; }

  .panel--green  { fill: var(--green); }
  .panel--yellow { fill: var(--yellow); }
  .panel--white  { fill: var(--white-panel); }
  .panel--red    { fill: var(--red); }
  .panel--blue   { fill: var(--blue); }

  .glyph {
    font-family: "Titan One", sans-serif;
    text-anchor: middle;
    dominant-baseline: central;
    stroke-linejoin: round;
  }
  .glyph--big { font-size: 104px; }
  .glyph-shadow { fill: var(--outline); stroke: var(--outline); stroke-width: 12px; }
  .glyph-edge   { fill: var(--outline); stroke: var(--outline); stroke-width: 12px; }
  .glyph-rim    { fill: var(--rim); stroke: var(--rim); stroke-width: 6px; }
  .glyph-face   { fill: var(--ink-blue); }

  .corner {
    font-family: "Titan One", sans-serif;
    font-size: 21px;
    text-anchor: middle;
    dominant-baseline: central;
    fill: var(--ink-blue);
    stroke: var(--outline);
    stroke-width: 4px;
    paint-order: stroke;
    stroke-linejoin: round;
  }
  .corner-rim {
    font-family: "Titan One", sans-serif;
    font-size: 21px;
    text-anchor: middle;
    dominant-baseline: central;
    fill: none;
    stroke: var(--rim);
    stroke-width: 1.2px;
  }

  .brand {
    font-family: "Titan One", sans-serif;
    font-size: 17px;
    fill: var(--ink-blue);
    text-anchor: middle;
    dominant-baseline: central;
  }
  .brand-mark { fill: var(--ink-blue); }

  .tick { fill: none; stroke-linecap: round; stroke-linejoin: round; }
  .tick-shadow { stroke: var(--outline); stroke-width: 34px; }
  .tick-edge   { stroke: var(--outline); stroke-width: 34px; }
  .tick-rim    { stroke: var(--rim); stroke-width: 28px; }
  .tick-face   { stroke: var(--ink-blue); stroke-width: 20px; }
  .tick-small-edge { stroke: var(--outline); stroke-width: 8px; }
  .tick-small-face { stroke: var(--ink-blue); stroke-width: 4.5px; }
</style>
</head>
<body>
<main class="card-row">

  <!-- Green number card -->
  <div class="card card--green">
    <svg viewBox="0 0 193 269" aria-label="Green card, number 7">
      <rect class="panel--green" x="10" y="10" width="173" height="249" rx="10"/>
      <g class="glyph glyph--big" transform="skewX(-8) translate(18 0)">
        <text class="glyph-shadow" x="101" y="140">7</text>
        <text class="glyph-edge" x="96.5" y="134">7</text>
        <text class="glyph-rim" x="96.5" y="134">7</text>
        <text class="glyph-face" x="96.5" y="134">7</text>
      </g>
      <text class="corner" x="31" y="32">7</text>
      <text class="corner" x="31" y="32" transform="rotate(180 96.5 134.5)">7</text>
    </svg>
  </div>

  <!-- Yellow number card -->
  <div class="card card--yellow">
    <svg viewBox="0 0 193 269" aria-label="Yellow card, number 12">
      <rect class="panel--yellow" x="10" y="10" width="173" height="249" rx="10"/>
      <g class="glyph glyph--big" transform="skewX(-8) translate(18 0)">
        <text class="glyph-shadow" x="101" y="140">12</text>
        <text class="glyph-edge" x="96.5" y="134">12</text>
        <text class="glyph-rim" x="96.5" y="134">12</text>
        <text class="glyph-face" x="96.5" y="134">12</text>
      </g>
      <text class="corner" x="34" y="32">12</text>
      <text class="corner" x="34" y="32" transform="rotate(180 96.5 134.5)">12</text>
    </svg>
  </div>

  <!-- White draw card -->
  <div class="card card--white">
    <svg viewBox="0 0 193 269" aria-label="White card, plus five">
      <rect class="panel--white" x="10" y="10" width="173" height="249" rx="10"/>
      <g class="brand-block">
        <rect class="brand-mark" x="96" y="34" width="10" height="10"/>
        <text class="brand" x="140" y="39">PILE UP</text>
      </g>
      <g class="brand-block" transform="rotate(180 96.5 134.5)">
        <rect class="brand-mark" x="96" y="34" width="10" height="10"/>
        <text class="brand" x="140" y="39">PILE UP</text>
      </g>
      <g class="glyph glyph--big" transform="skewX(-6) translate(14 0)">
        <text class="glyph-shadow" x="101" y="140">+5</text>
        <text class="glyph-edge" x="96.5" y="134">+5</text>
        <text class="glyph-rim" x="96.5" y="134">+5</text>
        <text class="glyph-face" x="96.5" y="134">+5</text>
      </g>
      <text class="corner" x="35" y="32">+5</text>
      <text class="corner" x="35" y="32" transform="rotate(180 96.5 134.5)">+5</text>
    </svg>
  </div>

  <!-- Red danger card -->
  <div class="card card--red">
    <svg viewBox="0 0 193 269" aria-label="Red card, exclamation mark">
      <rect class="panel--red" x="10" y="10" width="173" height="249" rx="10"/>
      <g class="glyph glyph--big" transform="skewX(-8) translate(18 0)">
        <text class="glyph-shadow" x="101" y="140">!</text>
        <text class="glyph-edge" x="96.5" y="134">!</text>
        <text class="glyph-rim" x="96.5" y="134">!</text>
        <text class="glyph-face" x="96.5" y="134">!</text>
      </g>
      <text class="corner" x="30" y="32">!</text>
      <text class="corner" x="30" y="32" transform="rotate(180 96.5 134.5)">!</text>
    </svg>
  </div>

  <!-- Blue joker card -->
  <div class="card card--blue">
    <svg viewBox="0 0 193 269" aria-label="Blue card, check mark">
      <rect class="panel--blue" x="10" y="10" width="173" height="249" rx="10"/>
      <g class="tick">
        <path class="tick-shadow" d="M66 150 L88 172 L146 106"/>
        <path class="tick-edge" d="M60 144 L82 166 L140 100"/>
        <path class="tick-rim" d="M60 144 L82 166 L140 100"/>
        <path class="tick-face" d="M60 144 L82 166 L140 100"/>
      </g>
      <g class="tick">
        <path class="tick-small-edge" d="M24 31 L29 37 L40 24"/>
        <path class="tick-small-face" d="M24 31 L29 37 L40 24"/>
      </g>
      <g class="tick" transform="rotate(180 96.5 134.5)">
        <path class="tick-small-edge" d="M24 31 L29 37 L40 24"/>
        <path class="tick-small-face" d="M24 31 L29 37 L40 24"/>
      </g>
    </svg>
  </div>

</main>
</body>
</html>
```